New Dental Office Needs an Attractive and user friendly Website Designed

I need a website for a new dental office. The Name is Maplecrest Dentistry. I would like a Modern design with a user friendly interface and usability.
I would like a landing page, a page that lists the services we offer: Cosmetic Dentistry, Implants, Dental Hygiene, Emergency Services, Restorations, Dentures
Target Market(s)
Mid to upper class
Industry/Entity Type
Dentistry
Coding
Coded - Design and coding required
Number of Pages Required
1 page
Requirements
Must have
- Landing page that has a scheduling option, Procedures, operating hours, and contact us info
Nice to have
- Appealing design, Soft comforting colors. Easy to navigate page, Modern and professional.

```html
<!DOCTYPE html>
<html lang="en">
<head>
<meta charset="utf-8">
<title>Maplecrest Dentistry</title>
<link href="https://fonts.googleapis.com/css2?family=Spectral:wght@400;500;600&family=Lato:wght@400;700&display=swap" rel="stylesheet">
<style>
:root{
  --teal-dark:#135f58;
  --teal:#1b6e62;
  --teal-bright:#26a48b;
  --mint:#d9eeea;
  --mint-box:#d5ebe6;
  --sage:#dde6e4;
  --cream:#f1ede7;
  --ink:#1f2a2a;
  --white:#fff;
}
*{margin:0;padding:0;box-sizing:border-box}
html,body{width:1200px;height:5164px;overflow:hidden}
body{font-family:"Lato",sans-serif;color:var(--ink);background:var(--white);position:relative}
section,header,footer,.topbar{position:absolute;left:0;width:1200px}
.abs{position:absolute;z-index:1}
.serif{font-family:"Spectral",serif;font-weight:400;color:var(--teal-dark);letter-spacing:2px}
.btn{position:absolute;z-index:1;display:flex;align-items:center;justify-content:center;background:var(--teal);color:var(--white);font-size:20px;border-radius:3px;text-decoration:none}
.photo{position:absolute;z-index:0}

.topbar{top:0;height:40px;background:var(--teal)}
.topbar .phone{left:96px;top:10px;color:#fff;font-size:15px;display:flex;gap:8px;align-items:center}
.topbar .social{right:90px;top:11px;display:flex;gap:10px}
.topbar .social span{width:18px;height:18px;background:#fff;border-radius:3px;display:block}

.site-header{top:40px;height:96px;border-bottom:2px solid #cfe3de}
.logo{font-family:"Spectral",serif;font-size:28px;color:var(--teal);font-weight:500}
.site-header .logo{left:96px;top:28px}
.nav{position:absolute;left:0;top:0;width:1200px;height:96px}
.nav a{position:absolute;top:36px;color:var(--teal-dark);font-size:18px;text-decoration:none;white-space:nowrap}

.hero{top:136px;height:538px;background:var(--cream);overflow:hidden}
.hero h1{left:88px;top:98px;font-size:58px;line-height:68px;font-weight:600;letter-spacing:1.5px;white-space:nowrap}
.hero p{left:88px;top:254px;font-size:27px;line-height:44px}

.about{top:674px;height:260px;background:var(--sage)}
.about h2{left:86px;top:88px;font-size:50px}
.about p{left:342px;top:84px;font-size:24px;line-height:31px;width:780px}

.services{top:934px;height:1014px}
.services h2{width:100%;text-align:center;top:92px;font-size:50px}
.services .sub{width:100%;text-align:center;top:166px;font-size:24px}
.service{position:absolute;width:340px;text-align:center}
.service svg{display:block;margin:0 auto}
.service h3{font-size:24px;font-weight:700;color:var(--teal-dark);margin-top:22px}
.service p{font-size:16px;line-height:24px;margin-top:8px;height:52px}
.service .btn{position:relative;margin:22px auto 0;width:158px;height:48px}

.cta{top:1948px;height:384px;background:var(--teal-dark)}
.cta h2{left:88px;top:86px;font-size:48px;color:#fff;font-weight:500}
.cta p{left:88px;top:160px;font-size:24px;line-height:35px;color:#e6f2ef}
.cta .btn{left:88px;top:258px;width:158px;height:46px;background:#fff;color:var(--teal-dark)}

.hours{top:2332px;height:952px}
.hours h2{left:90px;top:94px;font-size:50px;line-height:68px}
.hours .box{left:88px;top:280px;width:468px;height:378px;background:var(--mint-box);border-radius:10px;padding:36px 0 0 32px}
.hours table{border-collapse:collapse;font-size:24px}
.hours td{height:42.5px;padding:0}
.hours td:first-child{width:182px}
.hours .addr{left:106px;top:704px;font-size:24px;line-height:32px}
.hours .btn{left:106px;top:786px;width:188px;height:48px}

.reviews{top:3284px;height:580px;background:var(--teal-bright)}
.reviews h2{width:100%;text-align:center;top:96px;font-size:50px;color:#fff;font-weight:500}
.card{position:absolute;top:212px;width:320px;height:274px;background:#fff;border-radius:6px;padding:36px 44px 0;font-size:19px;line-height:34px}
.card .quote{font-family:"Spectral",serif;font-size:60px;line-height:40px;color:var(--teal-bright);font-weight:500;height:36px}
.card strong{display:block;margin-top:22px}

.book{top:3864px;height:552px}
.book h2{left:88px;top:122px;font-size:50px;line-height:68px}
.book p{left:88px;top:300px;font-size:24px;line-height:36px}
.book .btn{left:88px;top:392px;width:186px;height:48px}

.newsletter{top:4416px;height:382px;background:var(--mint)}
.newsletter h2{width:100%;text-align:center;top:84px;font-size:50px}
.newsletter p{width:100%;text-align:center;top:164px;font-size:24px}
.newsletter .field{left:306px;top:240px;width:394px;height:58px;background:#fff;font-size:20px;padding-left:38px;display:flex;align-items:center}
.newsletter .btn{left:700px;top:240px;width:194px;height:58px;background:var(--teal-bright);font-size:30px}

.site-footer{top:4798px;height:366px}
.site-footer .logo{width:100%;text-align:center;top:62px}
.site-footer .links{width:100%;top:152px;display:flex;justify-content:center;gap:50px;font-size:18px;color:var(--teal-dark)}
.site-footer .legal{width:100%;text-align:center;top:208px;font-size:18px;color:var(--teal-dark)}
.site-footer .copy{width:100%;text-align:center;top:266px;font-size:18px;color:var(--teal-dark)}
</style>
</head>
<body>

<div class="topbar">
  <div class="abs phone"><svg width="10" height="16" viewBox="0 0 10 16"><rect x="1" y="1" width="8" height="14" rx="2" fill="#fff"/></svg>(555) 014-2290</div>
  <div class="abs social"><span></span><span></span><span></span></div>
</div>

<header class="site-header">
  <div class="abs logo">Maplecrest Dentistry</div>
  <nav class="nav">
    <a style="left:552px">Services</a>
    <a style="left:684px">About</a>
    <a style="left:794px">Contact</a>
  </nav>
  <a class="btn" style="left:946px;top:20px;width:168px;height:52px;font-size:22px">Book Online</a>
</header>

<section class="hero">
  <div class="photo" role="img" aria-label="Smiling family of three: mother, young daughter and father" style="left:600px;top:0;width:600px;height:538px;background:linear-gradient(90deg,#f1ede7 0%,#eadfd2 30%,#e4d6c6 70%,#ece4da 100%)"></div>
  <h1 class="abs serif">Advance Care with<br>a Gentle Touch</h1>
  <p class="abs">Advanced Care with a Gentle Touch.<br>Because Your Smile Deserves the Best.</p>
  <a class="btn" style="left:86px;top:358px;width:270px;height:50px">Schedule Appointment</a>
</section>

<section class="about">
  <h2 class="abs serif">About Us</h2>
  <p class="abs">Providing exceptional dental care in a tranquil, spa-like setting.<br>We cater to your individual needs with state-of-the-art technology<br>and a gentle personal approach.</p>
</section>

<section class="services">
  <h2 class="abs serif">Our Services</h2>
  <p class="abs sub">Comprehensive Dental Solutions, Tailored to You.</p>

  <div class="service" style="left:82px;top:280px">
    <svg width="80" height="80" viewBox="0 0 80 80" fill="none" stroke="#1f2a2a" stroke-width="2.5"><path d="M22 16c-8 0-14 8-12 20 2 10 6 14 7 24 1 8 3 14 7 14 5 0 4-18 10-18s5 18 10 18c4 0 6-6 7-14 1-8 4-12 5-18"/><path d="M22 16c6 0 10 4 18 4"/><path d="M62 4l3 8 8 3-8 3-3 8-3-8-8-3 8-3z"/></svg>
    <h3>Cosmetic Dentistry</h3>
    <p>Whitening, veneers, and smile<br>makeovers for a confident appearance.</p>
    <a class="btn">Learn More</a>
  </div>
  <div class="service" style="left:430px;top:280px">
    <svg width="80" height="80" viewBox="0 0 80 80" fill="none" stroke="#1f2a2a" stroke-width="2.5"><path d="M26 6c-6 0-10 4-10 10 0 6 4 10 6 12h36c2-2 6-6 6-12 0-6-4-10-10-10-4 0-6 2-14 2S30 6 26 6z"/><path d="M22 28h36"/><path d="M30 36h20M32 46h16M34 56h12M36 66h8l-4 8z"/></svg>
    <h3>Dental Implants</h3>
    <p>Permanent tooth replacement<br>with natural look, feel, and function.</p>
    <a class="btn">Learn More</a>
  </div>
  <div class="service" style="left:776px;top:280px">
    <svg width="100" height="80" viewBox="0 0 100 80" fill="none" stroke="#1f2a2a" stroke-width="2.5"><path d="M14 74l56-44 4 4-56 44z"/><path d="M20 66l6 6M26 62l6 6"/><path d="M80 30c-4-4-4-10 0-18 4 8 4 14 0 18z"/></svg>
    <h3>Hygiene &amp; Cleanings</h3>
    <p>Thorough, professional cleanings<br>to protect your oral health.</p>
    <a class="btn">Learn More</a>
  </div>

  <div class="service" style="left:82px;top:642px">
    <svg width="80" height="80" viewBox="0 0 80 80" fill="none" stroke="#1f2a2a" stroke-width="2.5"><path d="M40 6l26 10v22c0 18-12 30-26 36C26 68 14 56 14 38V16z"/><path d="M34 26h12v10h10v12H46v10H34V48H24V36h10z"/></svg>
    <h3>Emergency Services</h3>
    <p>Prompt, compassionate care<br>when dental issues can't wait.</p>
    <a class="btn">Learn More</a>
  </div>
  <div class="service" style="left:430px;top:642px">
    <svg width="80" height="80" viewBox="0 0 80 80" fill="none" stroke="#1f2a2a" stroke-width="2.5"><path d="M24 6c-10 0-16 10-12 24 2 8 4 12 5 22 1 12 4 22 9 22 6 0 4-24 14-24s8 24 14 24c5 0 8-10 9-22 1-10 3-14 5-22 4-14-2-24-12-24-6 0-10 4-16 4S30 6 24 6z"/><path d="M26 18c-4 2-6 6-5 12"/></svg>
    <h3>Restorations</h3>
    <p>Repair and strengthen teeth<br>with expertly crafted solutions.</p>
    <a class="btn">Learn More</a>
  </div>
  <div class="service" style="left:776px;top:642px">
    <svg width="90" height="80" viewBox="0 0 90 80" fill="none" stroke="#1f2a2a" stroke-width="2.5"><path d="M8 28c8 10 22 14 37 14s29-4 37-14"/><path d="M8 28c0 14 16 26 37 26s37-12 37-26"/><path d="M18 36v8M28 40v9M38 42v10M52 42v10M62 40v9M72 36v8"/></svg>
    <h3>Dentures &amp; Partials</h3>
    <p>Custom full or partial dentures<br>designed for comfort and fit.</p>
    <a class="btn">Learn More</a>
  </div>
</section>

<section class="cta">
  <h2 class="abs serif">Time to Prioritize Yourself.</h2>
  <p class="abs">Book your appointment with Maplecrest Dentistry and experience<br>our calming environment and personalized attention first hand.</p>
  <a class="btn">Learn More</a>
</section>

<section class="hours">
  <h2 class="abs serif">Office Hours<br>&amp; Location</h2>
  <div class="abs box">
    <table>
      <tr><td>Monday</td><td>8:00 AM - 4:30 PM</td></tr>
      <tr><td>Tuesday</td><td>8:00 AM - 4:30 PM</td></tr>
      <tr><td>Wednesday</td><td>Closed</td></tr>
      <tr><td>Thursday</td><td>8:00 AM - 4:30 PM</td></tr>
      <tr><td>Friday</td><td>8:00 AM - 4:30 PM</td></tr>
      <tr><td>Saturday</td><td>Closed</td></tr>
      <tr><td>Sunday</td><td>Closed</td></tr>
    </table>
  </div>
  <p class="abs addr">2240 Orchard Lane Ste 104<br>Fairview, TN 37000</p>
  <a class="btn">Get Directions</a>
  <div class="photo" role="img" aria-label="Calm waiting room corner with a beige armchair, wooden side table and potted fig plant" style="left:616px;top:94px;width:496px;height:744px;border-radius:4px;background:linear-gradient(180deg,#efe8dc 0%,#ebe2d3 70%,#dccbb2 100%)"></div>
</section>

<section class="reviews">
  <h2 class="abs serif">What Our Patients Are Saying</h2>
  <div class="card" style="left:88px;text-align:center">
    <div class="quote" style="text-align:left">“</div>
    The staff is very friendly and professional. Highly recommend this office!
    <strong style="text-align:left">- Nora L</strong>
  </div>
  <div class="card" style="left:440px">
    <div class="quote">“</div>
    My experience with the Doctor was fantastic.<br>I feel confident in my smile.
    <strong>- Daniel P</strong>
  </div>
  <div class="card" style="left:792px;color:#2f8a7a">
    <div class="quote">“</div>
    I had an emergency and Got same-day treatment.<br>So grateful for the care!
    <strong style="color:var(--teal-dark)">- Grace T</strong>
  </div>
</section>

<section class="book">
  <div class="photo" role="img" aria-label="Smiling couple posing together" style="left:630px;top:0;width:570px;height:552px;background:linear-gradient(90deg,#e9e4dc 0%,#d6c6b4 50%,#c9c8bc 100%)"></div>
  <h2 class="abs serif">Book an<br>Appointment</h2>
  <p class="abs">Ready for a healthier smile?<br>Scheduling your visit is quick and easy.</p>
  <a class="btn">Schedule Now</a>
</section>

<section class="newsletter">
  <h2 class="abs serif">Subscribe to Our Newsletter</h2>
  <p class="abs">Stay up to date with our latest news and dental tips.</p>
  <div class="abs field">Enter your email address</div>
  <a class="btn">Subscribe</a>
</section>

<footer class="site-footer">
  <div class="abs logo">Maplecrest Dentistry</div>
  <div class="abs links"><span>Home</span><span>Services</span><span>About</span><span>Contact</span></div>
  <div class="abs legal">Privacy Policy | Terms</div>
  <div class="abs copy">© 2025 Maplecrest Dentistry. All rights reserved.</div>
</footer>

</body>
</html>
```